Boutique PEO needs a catchy snail mail and email marketing flyer

Our company provides services to our clients and co-employees throughout the entire life cycle of an employee's employment. It is very serious business to our clients' but we need a catchy message and look to attract the attention of prospective clients. I have attached some of the ideas we tried.

Target Market(s)

small to medium size companies

Font styles to use
Serif

Colors

Designer to choose colors to be used in the design.

```html
<!DOCTYPE html>
<html lang="en">
<head>
<meta charset="utf-8">
<title>PEO Flyers</title>
<link rel="stylesheet" href="https://fonts.googleapis.com/css2?family=Josefin+Sans:wght@400;600&family=Oswald:wght@500;600&display=swap">
<style>
  :root {
    --backdrop: #2f2f31;
    --purple-deep: #7a3597;
    --purple-mid: #9a4cad;
    --purple-light: #c46bb6;
    --band-light: #b76cc6;
    --band-soft: #9e56b6;
    --white: #ffffff;
    --photo-black: #050505;
    --photo-black-glow: #2a2a2c;
    --photo-grey-a: #6e6764;
    --photo-grey-b: #4a4240;
    --photo-brown: #5a4234;
  }
  * { box-sizing: border-box; margin: 0; padding: 0; }
  html, body {
    width: 1200px; height: 776px; overflow: hidden;
    background: var(--backdrop);
  }
  .flyer-pair {
    position: relative; width: 1200px; height: 776px;
    display: flex; justify-content: center; align-items: center; gap: 40px;
  }
  .flyer {
    position: relative; width: 470px; height: 660px; overflow: hidden;
    background: linear-gradient(160deg, var(--purple-deep) 0%, var(--purple-mid) 50%, var(--purple-light) 100%);
  }
  .flyer__art { position: absolute; inset: 0; width: 470px; height: 660px; }
  .flyer__headline {
    position: absolute; left: 20px; right: 20px; top: 458px;
    font-family: "Josefin Sans", sans-serif; font-weight: 400; font-size: 25px; line-height: 1.28;
    color: var(--white); text-align: center;
  }
  .flyer__call {
    position: absolute; left: 0; right: 0; top: 562px;
    display: flex; align-items: center; gap: 8px;
  }
  .flyer__call::before, .flyer__call::after {
    content: ""; flex: 1; height: 4px; background: var(--white);
  }
  .flyer__call-label {
    font-family: "Oswald", sans-serif; font-weight: 600; font-size: 20px;
    color: var(--white); line-height: 1;
  }
  .flyer__phone {
    position: absolute; left: 0; right: 0; top: 578px;
    font-family: "Oswald", sans-serif; font-weight: 500; font-size: 50px;
    color: var(--white); text-align: center; letter-spacing: 0.5px;
  }
</style>
</head>
<body>
<main class="flyer-pair">
  <article class="flyer flyer--hanging">
    <svg class="flyer__art" viewBox="0 0 470 660" aria-hidden="true">
      <circle cx="190" cy="150" r="312" fill="var(--band-soft)"/>
      <circle cx="190" cy="150" r="302" fill="var(--band-light)"/>
    </svg>
    <svg class="flyer__art" viewBox="0 0 470 660" role="img" aria-label="Photo of a white kitten hanging from a clothesline on a black background">
      <defs>
        <radialGradient id="hangingPhotoTone" cx="0.45" cy="0.45" r="0.6">
          <stop offset="0" stop-color="var(--photo-black-glow)"/>
          <stop offset="1" stop-color="var(--photo-black)"/>
        </radialGradient>
      </defs>
      <circle cx="190" cy="150" r="290" fill="url(#hangingPhotoTone)"/>
    </svg>
    <p class="flyer__headline">HR Issues and Complex Employment<br>Regulations have you hanging?<br>Hold On and</p>
    <div class="flyer__call"><span class="flyer__call-label">CALL A PEO</span></div>
    <p class="flyer__phone">0300 5550 246 813</p>
  </article>

  <article class="flyer flyer--thinking">
    <svg class="flyer__art" viewBox="0 0 470 660" aria-hidden="true">
      <circle cx="195" cy="120" r="307" fill="var(--band-soft)"/>
      <circle cx="195" cy="120" r="297" fill="var(--band-light)"/>
    </svg>
    <svg class="flyer__art" viewBox="0 0 470 660" role="img" aria-label="Photo of a thoughtful chimpanzee resting its chin on its hand against a grey background">
      <defs>
        <radialGradient id="thinkingPhotoTone" cx="0.35" cy="0.55" r="0.7">
          <stop offset="0" stop-color="var(--photo-brown)"/>
          <stop offset="0.55" stop-color="var(--photo-grey-b)"/>
          <stop offset="1" stop-color="var(--photo-grey-a)"/>
        </radialGradient>
      </defs>
      <circle cx="195" cy="120" r="285" fill="url(#thinkingPhotoTone)"/>
    </svg>
    <p class="flyer__headline">The Federal Government Does<br>Not Monkey Around When It<br>Comes To Enforcing Regulations</p>
    <div class="flyer__call"><span class="flyer__call-label">CALL A PEO</span></div>
    <p class="flyer__phone">0300 5550 246 813</p>
  </article>
</main>
</body>
</html>
```